Port Delridge is a new play by R. J. Halvorsen. The name Port Delridge refers to the location of the 1966 Brightwater - Tarrow Valley American football game. The play follows Joan Pelletier, who is approaching 70, as she unwillingly participates in a date dinner with Dennis Ashford, navigates the morning after at his apartment, and leaves, 15 months later, to take his granddaughter to college following her marriage to Dennis and his death. The play explores the definition of family, sex and aging, true love, overwhelming loss, political fanaticism, sexual assault, college football and “days of the week” panties. During the play, Joan tells lies, solves a mystery, picks a fight, critiques flavored condoms, loses her true love and survives. She lives her mother’s adage that “Being a woman is messy.” The poster will need an easily editable area for the theater and show time.

```html
<!DOCTYPE html>
<html lang="en">
<head>
<meta charset="utf-8">
<title>Port Delridge — A new play by R. J. Halvorsen</title>
<link rel="stylesheet" href="https://fonts.googleapis.com/css2?family=Fraunces:opsz,wght@9..144,800;9..144,900&family=Arimo:wght@400&display=swap">
<style>
  :root {
    --night: #231d1c;
    --night-edge: #1a1514;
    --title-red: #d9423f;
    --garment-red: #f5443f;
    --garment-shadow: #6b6360;
    --label-ink: #2a1e1c;
    --band-grey: #dcdcdb;
    --band-grey-dark: #cfcfce;
    --info-ink: #222222;
  }
  html, body {
    margin: 0;
    padding: 0;
    width: 809px;
    height: 1200px;
    overflow: hidden;
    background: var(--night);
  }
  .poster {
    position: relative;
    width: 809px;
    height: 1200px;
    overflow: hidden;
  }
  .stage {
    position: absolute;
    inset: 0 0 239px 0;
    background: radial-gradient(ellipse at 50% 40%, var(--night) 55%, var(--night-edge) 100%);
  }
  .play-title {
    position: absolute;
    top: 128px;
    left: 0;
    width: 100%;
    margin: 0;
    text-align: center;
    font-family: "Fraunces", Georgia, serif;
    font-weight: 900;
    font-size: 70px;
    line-height: 1;
    letter-spacing: 1px;
    color: var(--title-red);
  }
  .byline {
    position: absolute;
    top: 214px;
    left: 0;
    width: 100%;
    margin: 0;
    text-align: center;
    font-family: "Fraunces", Georgia, serif;
    font-weight: 800;
    font-size: 24px;
    color: var(--title-red);
  }
  .garment {
    position: absolute;
    top: 456px;
    left: 97px;
    width: 600px;
    height: 274px;
  }
  .garment svg {
    display: block;
    width: 100%;
    height: 100%;
  }
  .day-label {
    position: absolute;
    top: 510px;
    left: 97px;
    width: 600px;
    margin: 0;
    text-align: center;
    font-family: "Fraunces", Georgia, serif;
    font-weight: 900;
    font-size: 50px;
    line-height: 1;
    color: var(--label-ink);
  }
  .show-info {
    position: absolute;
    left: 0;
    bottom: 0;
    width: 100%;
    height: 239px;
    background: linear-gradient(180deg, var(--band-grey) 0%, var(--band-grey-dark) 100%);
    font-family: "Arimo", Arial, sans-serif;
    font-size: 22px;
    letter-spacing: 2px;
    color: var(--info-ink);
    text-align: center;
  }
  .show-time {
    position: absolute;
    top: 32px;
    left: 0;
    width: 100%;
    margin: 0;
  }
  .venue {
    position: absolute;
    top: 118px;
    left: 0;
    width: 100%;
    margin: 0;
  }
</style>
</head>
<body>
  <main class="poster">
    <section class="stage">
      <h1 class="play-title">PORT DELRIDGE</h1>
      <p class="byline">A new play by R. J. Halvorsen</p>
      <div class="garment">
        <svg viewBox="0 0 600 274" role="img" aria-label="Red days-of-the-week panties with a small pink bow">
          <rect x="6" y="8" width="594" height="266" fill="var(--garment-shadow)"/>
          <rect x="0" y="0" width="594" height="266" fill="var(--garment-red)"/>
        </svg>
      </div>
      <p class="day-label">SATURDAY</p>
    </section>
    <footer class="show-info">
      <p class="show-time">Show Time</p>
      <p class="venue">Theatre</p>
    </footer>
  </main>
</body>
</html>
```